Business Card Design Project

use presentation folder design and my logo and make 4 over 4 business cards

Industry/Entity Type

Business

Requirements
Must have
• use the design from my presentation folder and put my logo on it

Name
Title
phone
fax
email

```html
<!DOCTYPE html>
<html lang="en">
<head>
<meta charset="utf-8">
<title>Harborline Counseling – Business Cards</title>
<link rel="stylesheet" href="https://fonts.googleapis.com/css2?family=Quicksand:wght@400;500;600;700&display=swap">
<style>
  :root {
    --backdrop: #5d5d5d;
    --card-cream: #f3e4d9;
    --peach-light: #ebd2c0;
    --peach-mid: #dcb69c;
    --silver-light: #e6e3e0;
    --silver-mid: #cdc8c4;
    --tile-silver: #a9a7a6;
    --copper: #8c4a22;
    --ink: #2a2421;
  }
  html, body {
    margin: 0;
    padding: 0;
    width: 1200px;
    height: 1200px;
    overflow: hidden;
    background: var(--backdrop);
    font-family: "Quicksand", sans-serif;
  }
  .sheet {
    position: relative;
    width: 1200px;
    height: 1200px;
  }
  .card {
    position: absolute;
    left: 150px;
    width: 900px;
    height: 514px;
    overflow: hidden;
    box-shadow: 0 10px 30px rgba(0,0,0,0.35);
  }
  .card--contact { top: 40px; }
  .card--brand { top: 646px; }
  .card svg.card__art {
    position: absolute;
    inset: 0;
    width: 100%;
    height: 100%;
  }
  .brand-lockup {
    position: absolute;
    display: flex;
    align-items: center;
    gap: 14px;
    color: var(--copper);
    font-weight: 700;
    white-space: nowrap;
  }
  .brand-lockup__dot {
    border-radius: 50%;
    background: var(--copper);
    flex: none;
  }
  .card--contact .brand-lockup {
    top: 58px;
    right: 34px;
    font-size: 24px;
    gap: 10px;
  }
  .card--contact .brand-lockup__dot { width: 22px; height: 22px; }
  .card--brand .brand-lockup {
    top: 210px;
    left: 190px;
    font-size: 50px;
  }
  .card--brand .brand-lockup__dot { width: 46px; height: 46px; }

  .holder {
    position: absolute;
    left: 270px;
    top: 120px;
  }
  .holder__name {
    margin: 0;
    font-size: 40px;
    font-weight: 500;
    color: var(--ink);
    letter-spacing: 0.5px;
  }
  .holder__title {
    margin: 4px 0 0 150px;
    font-size: 20px;
    font-weight: 500;
    color: var(--copper);
  }
  .contact {
    position: absolute;
    left: 440px;
    top: 318px;
    font-size: 19px;
    line-height: 1.35;
    color: var(--ink);
  }
  .contact__row {
    display: flex;
    align-items: flex-start;
    gap: 10px;
  }
  .contact__row svg { flex: none; margin-top: 3px; }
  .contact__city { font-weight: 700; }
  .contact__phones { display: flex; gap: 40px; }
  .contact__phone { display: flex; align-items: center; gap: 10px; }
</style>
</head>
<body>
<main class="sheet">

  <section class="card card--contact">
    <svg class="card__art" viewBox="0 0 900 514" preserveAspectRatio="none">
      <defs>
        <linearGradient id="tileTones" x1="0" y1="0" x2="1" y2="1">
          <stop offset="0" stop-color="#b3b0ae"/>
          <stop offset="0.5" stop-color="#dcb49a"/>
          <stop offset="1" stop-color="#b9b6b4"/>
        </linearGradient>
        <linearGradient id="peachBand" x1="0" y1="0" x2="1" y2="1">
          <stop offset="0" stop-color="#e9cfbc"/>
          <stop offset="1" stop-color="#d6ad92"/>
        </linearGradient>
      </defs>
      <rect width="900" height="514" fill="var(--card-cream)"/>
      <polygon points="0,0 250,0 115,514 0,514" fill="url(#tileTones)" role="img" aria-label="Mosaic of silver and peach square tiles"/>
      <path d="M560,0 C720,60 835,260 900,514 L900,0 Z" fill="url(#peachBand)"/>
    </svg>

    <div class="brand-lockup"><span class="brand-lockup__dot"></span>Harborline Counseling</div>

    <header class="holder">
      <h1 class="holder__name">Daniel Whitford</h1>
      <p class="holder__title">Founder / CEO</p>
    </header>

    <address class="contact" style="font-style: normal;">
      <div class="contact__row">
        <svg width="16" height="20" viewBox="0 0 16 20"><path d="M8 0a7 7 0 0 0-7 7c0 5 7 13 7 13s7-8 7-13a7 7 0 0 0-7-7zm0 9.5A2.5 2.5 0 1 1 8 4.5a2.5 2.5 0 0 1 0 5z" fill="var(--ink)"/></svg>
        <div>Corporate Office<br>4810 Linden Ridge Rd. Suite 210<br><span class="contact__city">Marietta GA 30060</span></div>
      </div>
      <div class="contact__phones">
        <span class="contact__phone">
          <svg width="16" height="16" viewBox="0 0 16 16"><path d="M3 1l3 3-2 2c1 2 3 4 5 5l2-2 3 3-2 3C7 15 1 9 1 3z" fill="var(--ink)"/></svg>555.214.7730
        </span>
        <span class="contact__phone">
          <svg width="16" height="16" viewBox="0 0 16 16"><rect x="1" y="5" width="14" height="9" rx="1" fill="var(--copper)"/><rect x="4" y="1" width="8" height="5" fill="var(--copper)"/></svg>555.386.1942
        </span>
      </div>
      <div class="contact__row">
        <svg width="16" height="14" viewBox="0 0 16 14" style="margin-top:5px"><rect x="0" y="1" width="16" height="12" rx="1" fill="var(--ink)"/><path d="M1 2l7 6 7-6" stroke="#f3e4d9" stroke-width="1.5" fill="none"/></svg>
        <span>hello@harborlinecounseling.com</span>
      </div>
    </address>
  </section>

  <section class="card card--brand">
    <svg class="card__art" viewBox="0 0 900 514" preserveAspectRatio="none">
      <defs>
        <linearGradient id="silverFace" x1="0" y1="0" x2="0" y2="1">
          <stop offset="0" stop-color="#e8e5e2"/>
          <stop offset="1" stop-color="#c9c3bf"/>
        </linearGradient>
        <linearGradient id="peachCorner" x1="0" y1="0" x2="1" y2="1">
          <stop offset="0" stop-color="#e6c9b5"/>
          <stop offset="1" stop-color="#d3aa8e"/>
        </linearGradient>
      </defs>
      <rect width="900" height="514" fill="url(#silverFace)"/>
      <path d="M900,140 C790,250 660,410 590,514 L900,514 Z" fill="url(#peachCorner)"/>
    </svg>

    <div class="brand-lockup"><span class="brand-lockup__dot"></span>Harborline Counseling</div>
  </section>

</main>
</body>
</html>
```